We need a label design for our company, Ridgeline Botanica. We produce organic CBD oil and CBD infusing products. This label will be used on our new line of 1oz-3oz CBD oil. We would like the design to include our company logo and QR code, which I will add in the upload files area. The label should also have an area with our ingredients, which are:
CBD oil, Peppermint oil, Lavender oil, Eucalyptus oil, Cinnamon oil, Clove oil, and Vitamin E.
The final product should appeal to customer and be eye catching.

```html
<!DOCTYPE html>
<html lang="en">
<head>
<meta charset="utf-8">
<title>Ridgeline Botanica – CBD Oil Label</title>
<link rel="stylesheet" href="https://fonts.googleapis.com/css2?family=Poppins:wght@400;500;600&display=swap">
<style>
  :root {
    --backdrop: #c4eef6;
    --label-blue: #17457f;
    --band-blue-light: #3a6ab8;
    --leaf-green: #2a8a2a;
    --field-green-dark: #2c5e2b;
    --field-green-light: #3a8d37;
    --drop-green: #b9dc6a;
    --white: #ffffff;
  }
  * { box-sizing: border-box; margin: 0; padding: 0; }
  html, body {
    width: 1200px;
    height: 1200px;
    overflow: hidden;
    background: var(--backdrop);
    font-family: "Poppins", sans-serif;
  }
  .label {
    position: absolute;
    left: 219px;
    top: 61px;
    width: 762px;
    height: 1077px;
    overflow: hidden;
    background: linear-gradient(135deg, var(--field-green-dark) 0%, var(--field-green-light) 100%);
    box-shadow: 0 6px 14px rgba(0, 0, 0, 0.18);
  }
  .label-shapes {
    position: absolute;
    inset: 0;
    width: 762px;
    height: 1077px;
  }
  .foliage {
    position: absolute;
    left: 470px;
    top: 380px;
    width: 292px;
    height: 260px;
    background: radial-gradient(ellipse at 60% 50%, rgba(90, 170, 70, 0.45) 0%, rgba(90, 170, 70, 0) 70%);
  }
  .oil-drops {
    position: absolute;
    left: 372px;
    top: 495px;
    width: 365px;
    height: 490px;
    background: radial-gradient(ellipse at 62% 62%, rgba(205, 232, 130, 0.85) 0%, rgba(170, 215, 95, 0.55) 45%, rgba(120, 180, 70, 0) 72%);
  }
  .brand {
    position: absolute;
    left: 0;
    top: 60px;
    width: 762px;
    text-align: center;
  }
  .brand-dot {
    display: block;
    width: 120px;
    height: 120px;
    margin: 0 auto 34px;
    border-radius: 50%;
    background: var(--leaf-green);
  }
  .brand-name {
    font-size: 44px;
    font-weight: 500;
    letter-spacing: 3px;
    line-height: 1.15;
    color: var(--label-blue);
    text-transform: uppercase;
  }
  .ingredients {
    position: absolute;
    left: 46px;
    top: 568px;
    list-style: none;
  }
  .ingredient {
    display: flex;
    align-items: center;
    height: 60.8px;
    font-size: 33px;
    font-weight: 600;
    color: var(--white);
  }
  .tick {
    width: 26px;
    height: 26px;
    margin-right: 30px;
    margin-top: 6px;
    flex: none;
  }
  .size-band {
    position: absolute;
    left: 0;
    bottom: 0;
    width: 762px;
    height: 54px;
    background: linear-gradient(90deg, var(--label-blue) 0%, var(--label-blue) 45%, var(--band-blue-light) 100%);
    color: var(--white);
    font-size: 29px;
    font-weight: 400;
    text-align: center;
    line-height: 56px;
  }
</style>
</head>
<body>
  <main class="label">
    <div class="foliage" role="img" aria-label="Faint hemp leaves in the green field"></div>

    <svg class="label-shapes" viewBox="0 0 762 1077" aria-hidden="true">
      <circle cx="381" cy="123" r="420" fill="var(--label-blue)"/>
      <circle cx="381" cy="55" r="377" fill="var(--white)"/>
      <path d="M82 0 C56 80 60 180 117 268 C78 180 70 90 94 0 Z" fill="var(--leaf-green)"/>
      <path d="M680 0 C706 80 702 180 645 268 C684 180 692 90 668 0 Z" fill="var(--leaf-green)"/>
    </svg>

    <div class="oil-drops" role="img" aria-label="Two glistening oil droplets, each holding a hemp leaf"></div>

    <header class="brand">
      <span class="brand-dot"></span>
      <h1 class="brand-name">Ridgeline<br>Botanica</h1>
    </header>

    <ul class="ingredients">
      <li class="ingredient"><svg class="tick" viewBox="0 0 26 26"><circle cx="13" cy="13" r="11" fill="none" stroke="#fff" stroke-width="2"/><path d="M8 13.5l3.5 3.5L19 9" fill="none" stroke="#fff" stroke-width="2"/></svg>CBD oil,</li>
      <li class="ingredient"><svg class="tick" viewBox="0 0 26 26"><circle cx="13" cy="13" r="11" fill="none" stroke="#fff" stroke-width="2"/><path d="M8 13.5l3.5 3.5L19 9" fill="none" stroke="#fff" stroke-width="2"/></svg>Peppermint oil,</li>
      <li class="ingredient"><svg class="tick" viewBox="0 0 26 26"><circle cx="13" cy="13" r="11" fill="none" stroke="#fff" stroke-width="2"/><path d="M8 13.5l3.5 3.5L19 9" fill="none" stroke="#fff" stroke-width="2"/></svg>Lavender oil,</li>
      <li class="ingredient"><svg class="tick" viewBox="0 0 26 26"><circle cx="13" cy="13" r="11" fill="none" stroke="#fff" stroke-width="2"/><path d="M8 13.5l3.5 3.5L19 9" fill="none" stroke="#fff" stroke-width="2"/></svg>Eucalyptus oil,</li>
      <li class="ingredient"><svg class="tick" viewBox="0 0 26 26"><circle cx="13" cy="13" r="11" fill="none" stroke="#fff" stroke-width="2"/><path d="M8 13.5l3.5 3.5L19 9" fill="none" stroke="#fff" stroke-width="2"/></svg>Cinnamon oil,</li>
      <li class="ingredient"><svg class="tick" viewBox="0 0 26 26"><circle cx="13" cy="13" r="11" fill="none" stroke="#fff" stroke-width="2"/><path d="M8 13.5l3.5 3.5L19 9" fill="none" stroke="#fff" stroke-width="2"/></svg>Clove oil,</li>
      <li class="ingredient"><svg class="tick" viewBox="0 0 26 26"><circle cx="13" cy="13" r="11" fill="none" stroke="#fff" stroke-width="2"/><path d="M8 13.5l3.5 3.5L19 9" fill="none" stroke="#fff" stroke-width="2"/></svg>and Vitamin E.</li>
    </ul>

    <footer class="size-band">1oz-3oz CBD oil</footer>
  </main>
</body>
</html>
```